Election features for a political website

The Hearthside Ledger (www.hearthsideledger.example)
Web banner designs
Please have a look at The Hearthside Ledger website (www.hearthsideledger.example). We are seeking to add an advertising style banner at the top of every page and post. It will run right across the page (1024 pixels) and be in the region of 200 pixels vertically. (Please advise on what looks best size wise.
The banner will be a slider, operated in a similar way to the current homepage slider. There will be four items on the slider, and so we need four designs that match the aesthetic feel of the website. Each slider will link through to posts on the website.
1.
Headline: OUR CANDIDATE OF THE DAY
Space for a name, head and shoulders picture of the person to be dropped in and a one line reason. This will need to be in an editable format as this image will be changed each day for one month.
2.
Headline: HERO OF THE DAY
Space for name and a one line reason. This will need to be in an editable format as this image will be changed each day for one month.
3.
Headline: VILLAIN OF THE DAY
Space for name of the person to be dropped in and a one line reason. This will need to be in an editable format as this image will be changed each day for one month.
4.
Headline: THL Poll – [Date]
If the election was today, who would you vote for?
Clickable options:
Brightfolders
Ashvel
Marden Alliancers
Vornu
Tally
Other
Can a poll widget be added to the banner? We would like this poll to reset each day and then pool the results into a graph day by day over a one month period.
Reason: Payment is now guaranteed. We would like to see more options.

```html
<!DOCTYPE html>
<html lang="en">
<head>
<meta charset="utf-8">
<title>The Hearthside Ledger – Election slider banners</title>
<link rel="stylesheet" href="https://fonts.googleapis.com/css2?family=Tinos:ital,wght@0,700;1,700&display=swap">
<style>
  :root {
    --brand-blue: #00669b;
    --divider-grey: #808080;
    --paper: #ffffff;
    --ink-light: #ffffff;
  }
  * { margin: 0; padding: 0; box-sizing: border-box; }
  html, body { width: 1200px; height: 1062px; overflow: hidden; background: var(--paper); }
  body { position: relative; font-family: "Tinos", "Times New Roman", serif; font-weight: 700; }

  .banner { position: absolute; left: 0; width: 1200px; height: 236px; background: var(--paper); overflow: hidden; }
  .banner--candidate { top: 0; height: 233px; }
  .banner--villain { top: 275px; }
  .banner--hero { top: 553px; }
  .banner--poll { top: 828px; height: 234px; }

  .divider { position: absolute; left: 0; width: 1200px; background: var(--divider-grey); }
  .divider--one { top: 233px; height: 42px; }
  .divider--two { top: 511px; height: 42px; }
  .divider--three { top: 789px; height: 39px; }

  .panel { position: absolute; right: 0; background: var(--brand-blue); }

  .masthead {
    position: absolute; left: 10px; top: 10px;
    color: var(--brand-blue); font-size: 24px; line-height: 1.05;
    font-style: normal; font-weight: 700;
  }

  .headline {
    position: absolute; left: 670px; width: 530px; text-align: center;
    color: var(--ink-light); line-height: 1; white-space: nowrap;
  }
  .headline--caps { font-size: 80px; font-style: normal; letter-spacing: 1px; }
  .headline--script { font-size: 70px; font-style: italic; letter-spacing: 4px; }

  .reason {
    position: absolute; left: 690px; width: 520px; text-align: center;
    color: var(--ink-light); font-size: 36px; font-style: italic; line-height: 1; letter-spacing: 3px;
  }

  .candidate-reason {
    position: absolute; left: 10px; top: 140px;
    color: var(--brand-blue); font-size: 30px; font-style: italic; line-height: 1; letter-spacing: 2px; white-space: nowrap;
  }

  .person-name {
    position: absolute; color: var(--brand-blue);
    font-size: 42px; font-style: italic; line-height: 1; white-space: nowrap; letter-spacing: 2.5px;
  }

  .poll-options { position: absolute; left: 0; top: 0; width: 660px; height: 160px; list-style: none; }
  .poll-option {
    position: absolute; color: var(--brand-blue);
    font-size: 37px; font-style: italic; line-height: 1; white-space: nowrap; letter-spacing: 1.5px;
  }
  .poll-question {
    position: absolute; left: 313px; top: 177px;
    color: var(--ink-light); font-size: 36px; font-style: italic; line-height: 1; white-space: nowrap; letter-spacing: 2.4px;
  }
</style>
</head>
<body>

  <section class="banner banner--candidate" aria-label="Our candidate of the day">
    <div class="panel" style="left:820px; top:0; height:66px;"></div>
    <div class="panel" style="left:619px; top:66px; height:92px;"></div>
    <div class="panel" style="left:721px; top:158px; height:75px;"></div>
    <p class="masthead">The Hearthside<br>Ledger</p>
    <h2 class="headline headline--script" style="top:7px;">Our</h2>
    <h2 class="headline headline--caps" style="top:68px;">CANDIDATE</h2>
    <h2 class="headline headline--script" style="top:146px;">of the day</h2>
    <p class="candidate-reason">Reason here</p>
    <p class="person-name" style="left:9px; top:187px;">Full Name here</p>
  </section>

  <div class="divider divider--one"></div>

  <section class="banner banner--villain" aria-label="Villain of the day">
    <div class="panel" style="left:727px; top:0; height:67px;"></div>
    <div class="panel" style="left:660px; top:67px; height:93px;"></div>
    <div class="panel" style="left:702px; top:160px; height:76px;"></div>
    <p class="masthead" style="top:8px;">The Hearthside<br>Ledger</p>
    <h2 class="headline headline--caps" style="top:3px;">VILLAIN</h2>
    <h2 class="headline headline--script" style="top:78px;">of the day</h2>
    <p class="reason" style="top:181px;">Reason here</p>
    <p class="person-name" style="left:24px; top:190px;">Full Name here</p>
  </section>

  <div class="divider divider--two"></div>

  <section class="banner banner--hero" aria-label="Hero of the day">
    <div class="panel" style="left:769px; top:0; height:67px;"></div>
    <div class="panel" style="left:660px; top:67px; height:93px;"></div>
    <div class="panel" style="left:702px; top:160px; height:76px;"></div>
    <p class="masthead" style="top:8px;">The Hearthside<br>Ledger</p>
    <h2 class="headline headline--caps" style="top:2px;">HERO</h2>
    <h2 class="headline headline--script" style="top:78px;">of the day</h2>
    <p class="reason" style="top:194px;">Reason here</p>
    <p class="person-name" style="left:24px; top:190px;">Full Name here</p>
  </section>

  <div class="divider divider--three"></div>

  <section class="banner banner--poll" aria-label="THL poll">
    <div class="panel" style="left:726px; top:0; height:66px;"></div>
    <div class="panel" style="left:660px; top:66px; height:92px;"></div>
    <div class="panel" style="left:252px; top:158px; height:76px;"></div>
    <ul class="poll-options">
      <li class="poll-option" style="left:28px; top:13px;">Brightfolders</li>
      <li class="poll-option" style="left:28px; top:62px;">Marden Alliancers</li>
      <li class="poll-option" style="left:28px; top:111px;">Tally</li>
      <li class="poll-option" style="left:458px; top:13px;">Ashvel</li>
      <li class="poll-option" style="left:458px; top:62px;">Vornu</li>
      <li class="poll-option" style="left:454px; top:111px;">Other</li>
    </ul>
    <h2 class="headline headline--caps" style="top:0;">THL Poll</h2>
    <h2 class="headline headline--caps" style="top:73px;">[Date]</h2>
    <p class="poll-question">If the election was today, who would you vote for?</p>
  </section>

</body>
</html>
```